Business Cards for a small business advisory (business services)

Professional look. Same as would apply for a lawyer, accountant, or other financial services professional. Please use the logo colors

Target Market(s)

small business owners

Industry/Entity Type

Financial Servics

Contact Information for Business Card

Name: Gavin L. Whitmore, CAIA / Title: Business Advisor / Office #: (718) 294-7716 / Mobile #: (917) 382-5047 / Email: g.whitmore@clearfieldventurepartners.example / Web: www.clearfieldventurepartners.example

Font styles to use
Sans Serif

```html
<!DOCTYPE html>
<html lang="en">
<head>
<meta charset="utf-8">
<title>Clearfield Venture Partners – Business Cards</title>
<link href="https://fonts.googleapis.com/css2?family=Montserrat:wght@400;500;600;700&display=swap" rel="stylesheet">
<style>
  :root {
    --navy: #1d3a6b;
    --green: #8cc63f;
    --white: #ffffff;
    --ink: #1a1a1a;
    --backdrop: #9a9a9a;
  }
  * { margin: 0; padding: 0; box-sizing: border-box; }
  html, body {
    width: 1200px; height: 1059px; overflow: hidden;
    background: var(--backdrop);
    font-family: "Montserrat", sans-serif;
  }
  .card {
    position: absolute; left: 253px; width: 695px; height: 397px; overflow: hidden;
  }
  .card--front { top: 88px; background: var(--white); }
  .card--back { top: 569px; background: var(--navy); }

  .brand {
    position: absolute; left: 0; right: 0;
    display: flex; align-items: center; justify-content: center; gap: 24px;
  }
  .card--front .brand { top: 66px; }
  .card--back .brand { top: 146px; }
  .brand__dot {
    width: 96px; height: 96px; border-radius: 50%; background: var(--green); flex: none;
  }
  .card--back .brand__dot { background: var(--white); }
  .brand__text { display: flex; flex-direction: column; }
  .brand__name {
    font-weight: 600; color: var(--navy); line-height: 1; white-space: nowrap;
  }
  .card--back .brand__name { color: var(--white); }
  .brand__name--main { font-size: 70px; letter-spacing: -0.5px; }
  .brand__name--sub { font-size: 21px; letter-spacing: 3.4px; margin-top: 8px; }

  .person { position: absolute; left: 34px; top: 226px; }
  .person__name { font-size: 26px; font-weight: 700; color: var(--navy); line-height: 1.1; }
  .person__title { font-size: 18px; font-weight: 400; color: var(--ink); margin-top: 4px; }
  .divider {
    position: absolute; left: 36px; width: 636px; top: 296px; height: 1.5px; background: var(--ink);
  }
  .contact {
    position: absolute; display: flex; align-items: center; gap: 10px;
    color: var(--ink); font-size: 18px; white-space: nowrap;
  }
  .contact svg { width: 20px; height: 20px; fill: var(--navy); flex: none; }
  .contact--office { left: 34px; top: 309px; }
  .contact--mobile { left: 34px; top: 337px; }
  .contact--email { left: 252px; top: 309px; font-size: 15.6px; }
  .contact--web { left: 252px; top: 337px; font-size: 15.6px; }

  .band { position: absolute; bottom: 0; height: 15px; }
  .band--navy { left: 0; width: 511px; background: var(--navy); }
  .band--green { left: 511px; right: 0; background: var(--green); }
</style>
</head>
<body>

<section class="card card--front">
  <div class="brand">
    <div class="brand__dot"></div>
    <div class="brand__text">
      <span class="brand__name brand__name--main">Clearfield</span>
      <span class="brand__name brand__name--sub">VENTURE PARTNERS</span>
    </div>
  </div>

  <div class="person">
    <div class="person__name">Gavin L. Whitmore, CAIA</div>
    <div class="person__title">Business Advisor</div>
  </div>
  <div class="divider"></div>

  <div class="contact contact--office">
    <svg viewBox="0 0 24 24"><path d="M2 9c0-3 4-5 10-5s10 2 10 5v1.5h-5V8.5c-1.5-.6-3.2-.9-5-.9s-3.5.3-5 .9v2H2z"/><path d="M6 12l2-3h8l2 3v8H6z"/><circle cx="12" cy="15.5" r="2.3" fill="#fff"/></svg>
    <span>(718) 294-7716</span>
  </div>
  <div class="contact contact--mobile">
    <svg viewBox="0 0 24 24"><path d="M6.6 10.8c1.4 2.8 3.8 5.1 6.6 6.6l2.2-2.2c.3-.3.7-.4 1-.2 1.1.4 2.3.6 3.6.6.6 0 1 .4 1 1V20c0 .6-.4 1-1 1C10.6 21 3 13.4 3 4c0-.6.4-1 1-1h3.5c.6 0 1 .4 1 1 0 1.3.2 2.5.6 3.6.1.3 0 .7-.2 1z"/></svg>
    <span>(917) 382-5047</span>
  </div>
  <div class="contact contact--email">
    <svg viewBox="0 0 24 24"><path d="M2 5h20v14H2z"/><path d="M2 5l10 8 10-8M2 19l8-7M22 19l-8-7" stroke="#fff" stroke-width="1.6" fill="none"/></svg>
    <span>g.whitmore@clearfieldventurepartners.example</span>
  </div>
  <div class="contact contact--web">
    <svg viewBox="0 0 24 24"><circle cx="12" cy="12" r="9.5" fill="none" stroke="#1d3a6b" stroke-width="2"/><ellipse cx="12" cy="12" rx="4" ry="9.5" fill="none" stroke="#1d3a6b" stroke-width="1.8"/><path d="M2.5 12h19M4 7h16M4 17h16" stroke="#1d3a6b" stroke-width="1.6"/></svg>
    <span>www.clearfieldventurepartners.example</span>
  </div>

  <div class="band band--navy"></div>
  <div class="band band--green"></div>
</section>

<section class="card card--back">
  <div class="brand">
    <div class="brand__dot"></div>
    <div class="brand__text">
      <span class="brand__name brand__name--main">Clearfield</span>
      <span class="brand__name brand__name--sub">VENTURE PARTNERS</span>
    </div>
  </div>
</section>

</body>
</html>
```